Commercial Bakery needs packing design for a Bread Bag.

Dorne's Bakery needs a design for a bread bag to be distributed to grocery stores. We make all kinds of breads and want this packaging to represent our company. We would like the packaging to be black and white with a fun/bubbly modern design. I have attached a few ideas of what I am looking for.
There are 5 different products. Packaging must be the same for each product except for corresponding product name, bar code and nutrional facts.
Product names:
Coconut Cream Bread
Cream Bread
Potato Rolls
Roll ups
Coconut & Raisin Bread

Our products are packaged in a 11” x 8” poly bag.
I will open 5 contracts with whoever’s design I select. I will then provide nutritional facts, barcodes for items once a contract is selected. Thank you!!

Target Market(s)

Grocery stores

Industry/Entity Type

Bakery

Requirements
Must have
• Black and White (off whites are ok)
Should not have
• Color

```html
<!DOCTYPE html>
<html lang="en">
<head>
<meta charset="UTF-8">
<title>Dorne's Bakery – Bread Bag Labels</title>
<link rel="stylesheet" href="https://fonts.googleapis.com/css2?family=Archivo+Black&family=Montserrat:wght@600;800&display=swap">
<style>
  :root {
    --ink: #0d0d0d;
    --paper: #ffffff;
    --page: #ffffff;
    --edge: #e2e2e2;
  }
  * { box-sizing: border-box; margin: 0; padding: 0; }
  html, body {
    width: 1200px; height: 1200px; overflow: hidden;
    background: var(--page);
  }
  .canvas {
    width: 1200px; height: 1200px;
    display: flex; align-items: center; justify-content: center;
    gap: 35px;
  }
  .defs { position: absolute; width: 0; height: 0; }
  .label {
    position: relative;
    width: 200px; height: 277px;
    background: var(--paper);
    box-shadow: 0 0 0 1px var(--edge), 0 2px 6px rgba(0,0,0,0.08);
    overflow: hidden;
  }
  .label-dark {
    position: absolute; inset: 0;
    width: 200px; height: 277px;
  }
  .brand-seal {
    position: absolute;
    left: 50%; top: 52px;
    transform: translateX(-50%);
    width: 92px; height: 92px;
    border-radius: 50%;
    background: var(--paper);
    border: 2px solid var(--ink);
    display: flex; align-items: center; justify-content: center;
  }
  .brand-name {
    font-family: "Archivo Black", sans-serif;
    font-size: 15px;
    color: var(--ink);
  }
  .product-name {
    position: absolute;
    left: 14px; top: 176px;
    width: 82px;
    font-family: "Archivo Black", sans-serif;
    font-size: 12px;
    line-height: 1.05;
    text-transform: uppercase;
    color: var(--ink);
  }
  .product-name.single { top: 182px; }
  .nutrition-panel {
    position: absolute;
    left: 114px; top: 165px;
    width: 74px; height: 46px;
    background: var(--paper);
    border: 1px solid var(--ink);
    padding: 2px 3px;
    font-family: Montserrat, sans-serif;
    color: var(--ink);
  }
  .nutrition-title {
    font-weight: 800; font-size: 6px;
    border-bottom: 1px solid var(--ink);
    padding-bottom: 1px; margin-bottom: 1px;
  }
  .nutrition-row {
    display: flex; justify-content: space-between;
    font-weight: 600; font-size: 4.4px; line-height: 1.35;
    border-bottom: 0.5px solid var(--ink);
  }
  .nutrition-row.calories { font-weight: 800; font-size: 5.4px; }
  .net-weight {
    position: absolute;
    left: 14px; bottom: 12px;
    font-family: Montserrat, sans-serif;
    font-weight: 600; font-size: 5px;
    letter-spacing: 0.3px;
    color: var(--ink);
  }
</style>
</head>
<body>
<svg class="defs" aria-hidden="true">
  <defs>
    <pattern id="teeth" width="8" height="14" patternUnits="userSpaceOnUse">
      <polygon points="8,0 0,7 8,14" fill="#0d0d0d"/>
    </pattern>
  </defs>
</svg>

<main class="canvas">

  <article class="label">
    <svg class="label-dark" viewBox="0 0 200 277" role="img" aria-label="Black panel with a scattered wheat pattern">
      <rect x="96" y="0" width="8" height="277" fill="url(#teeth)"/>
      <rect x="104" y="0" width="96" height="277" fill="#0d0d0d"/>
    </svg>
    <div class="brand-seal"><span class="brand-name">Dorne's</span></div>
    <h2 class="product-name">Coconut Cream Bread</h2>
    <div class="nutrition-panel">
      <div class="nutrition-title">Nutrition Facts</div>
      <div class="nutrition-row"><span>Serving</span><span>1 slice</span></div>
      <div class="nutrition-row calories"><span>Calories</span><span>230</span></div>
      <div class="nutrition-row"><span>Fat</span><span>2g</span></div>
      <div class="nutrition-row"><span>Sodium</span><span>180mg</span></div>
    </div>
    <p class="net-weight">NET WT. 16 OZ</p>
  </article>

  <article class="label">
    <svg class="label-dark" viewBox="0 0 200 277" role="img" aria-label="Black panel with a scattered wheat pattern">
      <rect x="96" y="0" width="8" height="277" fill="url(#teeth)"/>
      <rect x="104" y="0" width="96" height="277" fill="#0d0d0d"/>
    </svg>
    <div class="brand-seal"><span class="brand-name">Dorne's</span></div>
    <h2 class="product-name">Coconut &amp; Raisin Bread</h2>
    <div class="nutrition-panel">
      <div class="nutrition-title">Nutrition Facts</div>
      <div class="nutrition-row"><span>Serving</span><span>1 slice</span></div>
      <div class="nutrition-row calories"><span>Calories</span><span>230</span></div>
      <div class="nutrition-row"><span>Fat</span><span>2g</span></div>
      <div class="nutrition-row"><span>Sodium</span><span>180mg</span></div>
    </div>
    <p class="net-weight">NET WT. 16 OZ</p>
  </article>

  <article class="label">
    <svg class="label-dark" viewBox="0 0 200 277" role="img" aria-label="Black panel with a scattered wheat pattern">
      <rect x="96" y="0" width="8" height="277" fill="url(#teeth)"/>
      <rect x="104" y="0" width="96" height="277" fill="#0d0d0d"/>
    </svg>
    <div class="brand-seal"><span class="brand-name">Dorne's</span></div>
    <h2 class="product-name single">Roll Ups</h2>
    <div class="nutrition-panel">
      <div class="nutrition-title">Nutrition Facts</div>
      <div class="nutrition-row"><span>Serving</span><span>1 slice</span></div>
      <div class="nutrition-row calories"><span>Calories</span><span>230</span></div>
      <div class="nutrition-row"><span>Fat</span><span>2g</span></div>
      <div class="nutrition-row"><span>Sodium</span><span>180mg</span></div>
    </div>
    <p class="net-weight">NET WT. 16 OZ</p>
  </article>

  <article class="label">
    <svg class="label-dark" viewBox="0 0 200 277" role="img" aria-label="Black panel with a scattered wheat pattern">
      <rect x="96" y="0" width="8" height="277" fill="url(#teeth)"/>
      <rect x="104" y="0" width="96" height="277" fill="#0d0d0d"/>
    </svg>
    <div class="brand-seal"><span class="brand-name">Dorne's</span></div>
    <h2 class="product-name">Potato Rolls</h2>
    <div class="nutrition-panel">
      <div class="nutrition-title">Nutrition Facts</div>
      <div class="nutrition-row"><span>Serving</span><span>1 slice</span></div>
      <div class="nutrition-row calories"><span>Calories</span><span>230</span></div>
      <div class="nutrition-row"><span>Fat</span><span>2g</span></div>
      <div class="nutrition-row"><span>Sodium</span><span>180mg</span></div>
    </div>
    <p class="net-weight">NET WT. 16 OZ</p>
  </article>

  <article class="label">
    <svg class="label-dark" viewBox="0 0 200 277" role="img" aria-label="Black panel with a scattered wheat pattern">
      <rect x="96" y="0" width="8" height="277" fill="url(#teeth)"/>
      <rect x="104" y="0" width="96" height="277" fill="#0d0d0d"/>
    </svg>
    <div class="brand-seal"><span class="brand-name">Dorne's</span></div>
    <h2 class="product-name">Cream Bread</h2>
    <div class="nutrition-panel">
      <div class="nutrition-title">Nutrition Facts</div>
      <div class="nutrition-row"><span>Serving</span><span>1 slice</span></div>
      <div class="nutrition-row calories"><span>Calories</span><span>230</span></div>
      <div class="nutrition-row"><span>Fat</span><span>2g</span></div>
      <div class="nutrition-row"><span>Sodium</span><span>180mg</span></div>
    </div>
    <p class="net-weight">NET WT. 16 OZ</p>
  </article>

</main>
</body>
</html>
```